Willowmere Haven tri-fold brochure

We are a small assisted living in a home-like environment. Brochure should be warm, heartfelt and include the list of services we provide (see existing brochure). I also want the front picture replaced with stock photo (so no picture of owners). New name to use (instead of Dorian) is Dorian Feltrowe, and email is feltrowe@quintmail.example. Address is same. If you can find better photos, that would be good, all the photos here are dated. We are looking for a more professional design that still conveys warmth, because we are in a home-setting and only care for 9 residents.

Target Market(s)

35-55 year old children looking for an assisted living because their parents are unable to care for them.

Industry/Entity Type

Environment

Contact Information for Business Card

Dorian Feltrowe
Willowmere Haven or Willowmere Haven Assisted Living
40718 Pinegrove Ln. Conroe, TX 77519
281-647-5192

Requirements
Must have
• List of services offered (feel free to re-word or add/change)
• Be sure to change "Hester/Hestie" to Dorian / Dorian Feltrowe

```html
<!DOCTYPE html>
<html lang="en">
<head>
<meta charset="utf-8">
<title>Willowmere Haven – Tri-fold Brochure</title>
<link href="https://fonts.googleapis.com/css2?family=Mulish:wght@300;400;500;600&family=Exo+2:wght@300;400&display=swap" rel="stylesheet">
<style>
  :root {
    --ink: #111111;
    --paper: #ffffff;
    --night: #000000;
    --sun: #ffc700;
    --frame: #fff35a;
    --photo-warm: #d9cfc7;
    --photo-soft: #e9e4df;
    --photo-sky: #c9d6e2;
    --photo-tea: #b9b0a8;
  }
  * { box-sizing: border-box; margin: 0; padding: 0; }
  html, body { width: 1200px; height: 848px; overflow: hidden; background: var(--paper); }
  body { font-family: "Mulish", "Helvetica Neue", Arial, sans-serif; color: var(--ink); }

  .brochure { position: relative; width: 1200px; height: 848px; background: var(--paper); }
  .sheet {
    position: absolute;
    left: 14px; top: 17px; width: 1172px; height: 815px;
    border: 1px solid #444;
    overflow: hidden;
  }
  .panel { position: absolute; top: 0; height: 100%; }

  /* Left panel – testimonials */
  .panel--testimonial { left: 0; width: 389px; background: var(--paper); }
  .panel-title {
    position: absolute; top: 32px; left: 0; width: 100%;
    text-align: center; font-size: 23px; font-weight: 400;
  }
  .framed-photo {
    position: absolute; left: 29px; width: 332px;
    border: 2px solid var(--frame); padding: 5px;
  }
  .framed-photo .photo { width: 100%; height: 100%; }
  .framed-photo--top { top: 64px; height: 225px; }
  .framed-photo--bottom { top: 646px; height: 160px; }
  .photo--carer-hands { background: linear-gradient(120deg, var(--photo-sky) 0%, var(--photo-soft) 45%, var(--photo-warm) 100%); }
  .photo--nurse-resident { background: linear-gradient(100deg, var(--photo-warm) 0%, var(--photo-soft) 55%, #cfe5e2 100%); }

  .testimonials {
    position: absolute; top: 302px; left: 13px; width: 335px;
    font-size: 15px; line-height: 1.38;
  }
  .testimonials p { margin-bottom: 20px; }
  .testimonials p:last-child { margin-bottom: 0; }

  /* Middle panel */
  .panel--middle { left: 389px; width: 502px; background: var(--night); color: var(--paper); }
  .middle-heading {
    position: absolute; top: 29px; left: 0; width: 395px;
    text-align: center; font-family: "Exo 2", "Mulish", sans-serif;
    font-weight: 300; font-size: 23px; line-height: 1.35;
  }
  .middle-intro {
    position: absolute; top: 153px; left: 30px; width: 335px;
    text-align: center; font-size: 15px; line-height: 1.38;
  }
  .photo--tea-couple {
    position: absolute; left: 3px; top: 259px; width: 386px; height: 267px;
    background: linear-gradient(90deg, var(--photo-tea) 0%, var(--photo-soft) 50%, #a89c92 100%);
  }
  .photo-strip { position: absolute; left: 395px; top: 174px; width: 104px; }
  .photo-strip .thumb { position: absolute; left: 0; width: 104px; }
  .thumb--1 { top: 0; height: 105px; background: linear-gradient(135deg, #d8c4b0, #eae3dc); }
  .thumb--2 { top: 122px; height: 103px; background: linear-gradient(135deg, #c7d2df, #e6e1dc); }
  .thumb--3 { top: 241px; height: 104px; background: linear-gradient(135deg, #e5ddd6, #cdbfb3); }
  .thumb--4 { top: 360px; height: 106px; background: linear-gradient(135deg, #efebe6, #d5cdc4); }

  .middle-cta {
    position: absolute; top: 596px; left: 45px; width: 305px;
    text-align: center; color: var(--sun); font-size: 15px; line-height: 1.38;
  }
  .address-block {
    position: absolute; left: 0; bottom: 0; width: 392px; height: 104px;
    background: var(--sun); color: var(--ink); font-style: normal;
    display: flex; flex-direction: column; align-items: center; justify-content: center;
    font-size: 15px; line-height: 1.4; text-align: center;
  }

  /* Right panel – cover */
  .panel--cover { left: 891px; width: 281px; background: var(--sun); }
  .brand-name {
    position: absolute; top: 62px; left: 20px; width: 250px;
    font-family: "Exo 2", "Mulish", sans-serif; font-weight: 300;
    font-size: 42px; line-height: 1.2;
  }
  .tagline {
    position: absolute; top: 197px; left: 22px; width: 240px;
    text-align: center; font-size: 15px; line-height: 1.38;
  }
  .services {
    position: absolute; top: 330px; left: 22px; width: 240px;
    text-align: center;
  }
  .services-title {
    font-family: "Exo 2", "Mulish", sans-serif; font-weight: 400;
    font-size: 20px; margin-bottom: 12px;
  }
  .services-list { list-style: none; font-size: 15px; line-height: 1.9; }
  .contact-name {
    position: absolute; top: 716px; left: 0; width: 100%;
    text-align: center; font-family: "Exo 2", "Mulish", sans-serif;
    font-size: 23px; font-weight: 400;
  }
  .contact-phone {
    position: absolute; top: 748px; left: 0; width: 100%;
    text-align: center; font-family: "Exo 2", "Mulish", sans-serif;
    font-size: 32px; font-weight: 400;
  }
</style>
</head>
<body>
<main class="brochure">
  <div class="sheet">

    <section class="panel panel--testimonial">
      <h2 class="panel-title">Testimonial</h2>
      <div class="framed-photo framed-photo--top">
        <div class="photo photo--carer-hands" role="img" aria-label="Caregiver holding the hands of a smiling elderly woman"></div>
      </div>
      <div class="testimonials">
        <p>• My Mom lived in five private care homes. When she moved to Dorian’s she said, “I’ve finally found my home.”</p>
        <p>•&nbsp; I lived in a facility where everything seems to be...door ….,door…,door…<br>Here is small, familiar and comfortable”</p>
        <p>•&nbsp; “I’d be miserable in a nursing home!”<br>If you are one of the millions of people who feel this way, we say,</p>
        <p>“Trust your instincts”</p>
        <p>Discover that smaller is better where full service care is provided in a real home.</p>
      </div>
      <div class="framed-photo framed-photo--bottom">
        <div class="photo photo--nurse-resident" role="img" aria-label="Young nurse embracing a senior woman"></div>
      </div>
    </section>

    <section class="panel panel--middle">
      <h2 class="middle-heading">Smaller is better When it comes<br>to the elderly.</h2>
      <p class="middle-intro">Our unique homes are designed to make the surroundings familiar and the care consistent.</p>
      <div class="photo--tea-couple" role="img" aria-label="Elderly couple laughing together over cups of tea on a sofa"></div>
      <div class="photo-strip">
        <div class="thumb thumb--1" role="img" aria-label="Daughter and senior father smiling together"></div>
        <div class="thumb thumb--2" role="img" aria-label="Son and senior father taking a photo together"></div>
        <div class="thumb thumb--3" role="img" aria-label="Senior woman hugging her daughter"></div>
        <div class="thumb thumb--4" role="img" aria-label="Senior woman enjoying a cup of tea"></div>
      </div>
      <p class="middle-cta">Please call for the personal tour and experience the Willowmere Haven difference</p>
      <address class="address-block">
        <span>40718 Pinegrove Ln.</span>
        <span>Conroe, Texas</span>
        <span>feltrowe@quintmail.example</span>
      </address>
    </section>

    <section class="panel panel--cover">
      <h1 class="brand-name">Willowmere Haven</h1>
      <p class="tagline">Offering a true and noble commitment to the highest standards of care in the industry</p>
      <div class="services">
        <h3 class="services-title">Our Services</h3>
        <ul class="services-list">
          <li>24-hour caring staff</li>
          <li>Home-cooked meals</li>
          <li>Medication management</li>
          <li>Bathing &amp; personal care</li>
          <li>Housekeeping &amp; laundry</li>
          <li>Daily activities &amp; outings</li>
        </ul>
      </div>
      <p class="contact-name">Dorian Feltrowe</p>
      <p class="contact-phone">281-647-5192</p>
    </section>

  </div>
</main>
</body>
</html>
```